Need a business card for our overland brand!

We had the logo made and we need a great design for our business card. Use the logo provide or tweak it however you see fit.

Contact Information for Business Card

Name, Title, Telephone, email, website

```html
<!DOCTYPE html>
<html lang="en">
<head>
<meta charset="utf-8">
<title>Ridgeline Expeditions – Business Card</title>
<link rel="stylesheet" href="https://fonts.googleapis.com/css2?family=Oswald:wght@600;700&family=Montserrat:wght@400;500&display=swap">
<style>
  :root {
    --navy: #1f3450;
    --navy-deep: #1b2e47;
    --teal: #2596b8;
    --card-white: #f7f7f7;
    --ink: #22364f;
    --backdrop: #d8d9db;
  }
  * { margin: 0; padding: 0; box-sizing: border-box; }
  html, body {
    width: 1200px;
    height: 900px;
    overflow: hidden;
    background: var(--backdrop);
  }
  .stage {
    position: relative;
    width: 1200px;
    height: 900px;
  }
  .card {
    position: absolute;
    top: 118px;
    width: 380px;
    height: 664px;
    box-shadow: 0 6px 18px rgba(0,0,0,0.18);
  }
  .card--front {
    left: 170px;
    background: var(--card-white);
  }
  .card--back {
    left: 650px;
    background: linear-gradient(160deg, var(--navy) 0%, var(--navy-deep) 100%);
  }
  .brand-name {
    position: absolute;
    left: 0;
    right: 0;
    text-align: center;
    font-family: "Oswald", sans-serif;
    font-weight: 700;
    text-transform: uppercase;
    line-height: 0.95;
    letter-spacing: 0.5px;
  }
  .card--front .brand-name {
    top: 118px;
    font-size: 48px;
    color: var(--navy);
  }
  .card--back .brand-name {
    top: 270px;
    font-size: 48px;
    color: #ffffff;
  }
  .contact-block {
    position: absolute;
    left: 84px;
    top: 392px;
    font-family: "Montserrat", sans-serif;
    color: var(--ink);
  }
  .person-name {
    font-family: "Oswald", sans-serif;
    font-weight: 600;
    font-size: 34px;
    line-height: 1;
    text-transform: uppercase;
    letter-spacing: 0.3px;
    color: var(--navy);
  }
  .person-name .first { color: var(--teal); }
  .person-title {
    margin-top: 4px;
    font-size: 16px;
    font-weight: 500;
  }
  .address {
    margin-top: 22px;
    font-size: 14px;
    line-height: 1.45;
  }
  .contact-list {
    list-style: none;
    margin-top: 22px;
    font-size: 14px;
    line-height: 1.6;
  }
  .contact-list li {
    display: flex;
    align-items: center;
    gap: 7px;
  }
  .contact-icon {
    width: 13px;
    height: 13px;
    flex: none;
  }
</style>
</head>
<body>
<main class="stage">
  <section class="card card--front" aria-label="Business card front">
    <h1 class="brand-name">Ridgeline<br>Expeditions</h1>
    <div class="contact-block">
      <p class="person-name"><span class="first">Daniel</span> Hart</p>
      <p class="person-title">Founder</p>
      <p class="address">2750 North Cedar Avenue<br>#14, Suite Pine Hollow</p>
      <ul class="contact-list">
        <li>
          <svg class="contact-icon" viewBox="0 0 16 16" aria-hidden="true">
            <path d="M4 1.5l2.2 3-1.3 1.6c.8 1.9 2.2 3.3 4.1 4.1l1.6-1.3 3 2.2-1 2.6C7.5 13.6 2.4 8.5 1.3 2.5z" fill="var(--teal)"/>
          </svg>
          <span>+1- 555-014-2290</span>
        </li>
        <li>
          <svg class="contact-icon" viewBox="0 0 16 16" aria-hidden="true">
            <rect x="1.5" y="3.5" width="13" height="9" rx="1" fill="none" stroke="var(--teal)" stroke-width="1.5"/>
            <path d="M2 4l6 5 6-5" fill="none" stroke="var(--teal)" stroke-width="1.5"/>
          </svg>
          <span>hello@ridgelineexp.com</span>
        </li>
        <li>
          <svg class="contact-icon" viewBox="0 0 16 16" aria-hidden="true">
            <circle cx="8" cy="8" r="6.5" fill="none" stroke="var(--teal)" stroke-width="1.4"/>
            <ellipse cx="8" cy="8" rx="2.8" ry="6.5" fill="none" stroke="var(--teal)" stroke-width="1.2"/>
            <path d="M1.5 8h13M2.5 5h11M2.5 11h11" stroke="var(--teal)" stroke-width="1.1"/>
          </svg>
          <span>www.ridgelineexp.com</span>
        </li>
      </ul>
    </div>
  </section>

  <section class="card card--back" aria-label="Business card back">
    <p class="brand-name">Ridgeline<br>Expeditions</p>
  </section>
</main>
</body>
</html>
```